Blog Banner Design Project: Notes For Wanderers

Looking for a new banner for my blog " Colin Ashworth's Notes for Wanderers" at http://www.notesforwanderers.example - and once design agreed also want an updated album art for the podcast that goes along with the site.
For more about the blog and what it is about:
http://www.notesforwanderers.example/about
Notes for Wanderers is a Luxury Travel Blog And Podcast that provides inspiration, advice and tips about luxurious travel experiences, including destinations, transportation, accommodation, and journeys, that travellers can read, listen to or watch.
Objective of the new design
(1) retain the colour scheme ideally to retain the brand identity, as have been using these colours since 2005.
(2) introduce more of my personality and make it more visually and overt that it is "Colin Ashworth's Notes for Wanderers", so possibly introducing my image into the blog banner so visitors are clear and more aware of the person behind the brand.
(3) needs to have an up-market, luxury but modern feel.
(4) if possible reflect the focus on the content (destinations, transportation, accommodation, attractions and journeys) - but this maybe best left to just words as want the design to be bold and more of the branding and personality.
Ideal wording
Smallish: Colin Ashworth's
Main wording: Notes for Wanderers
Sub-title/ small: luxurious destinations, transportation, accommodation and journeys.
Updates
I have a poll running with readers of my blog to rate the designs to help me to chose the final route, and so there is no need to submit any more designs. I will make the decision once the poll closes on the weekend.

```html
<!DOCTYPE html>
<html lang="en">
<head>
<meta charset="utf-8">
<title>Colin Ashworth's Notes for Wanderers – Banner Options</title>
<link href="https://fonts.googleapis.com/css2?family=Alegreya:wght@400;500&family=Josefin+Sans:wght@400&display=swap" rel="stylesheet">
<style>
  :root {
    --orange: #ffae00;
    --orange-light: #ffc43d;
    --purple: #a12fa8;
    --purple-light: #c25ac8;
    --black: #000000;
    --white: #ffffff;
    --stage: #2e2e2e;
    --stage-dark: #1c1c1c;
  }
  html, body {
    margin: 0;
    padding: 0;
    width: 1200px;
    height: 1000px;
    overflow: hidden;
  }
  body {
    position: relative;
    background: radial-gradient(ellipse at center, var(--stage) 0%, var(--stage-dark) 100%);
  }
  .banner {
    position: absolute;
    left: 114px;
    width: 960px;
    height: 136px;
    background: var(--black);
    overflow: hidden;
  }
  .banner--one   { top: 68px; }
  .banner--two   { top: 312px; }
  .banner--three { top: 556px; }
  .banner--four  { top: 800px; }

  .banner__sky {
    position: absolute;
    left: 0; top: 0;
    width: 960px;
    height: 67px;
    background: var(--orange);
  }
  .banner__skyline {
    position: absolute;
    left: 340px;
    top: 18px;
    width: 620px;
    height: 50px;
    background: linear-gradient(to bottom, rgba(0,0,0,0) 0%, rgba(0,0,0,0.55) 55%, var(--black) 100%);
  }
  .banner__name-band {
    position: absolute;
    left: 0;
    top: 32px;
    width: 175px;
    height: 28px;
    background: var(--purple);
  }
  .banner__portrait {
    position: absolute;
    left: 0; top: 0;
    width: 180px;
    height: 136px;
    background: linear-gradient(to right, #5f6670 0%, #3a4250 55%, rgba(0,0,0,0) 100%),
                linear-gradient(to bottom, #c99a7e 0%, #9a7564 45%, #263040 70%, #1b2230 100%);
  }
  .banner__first-name {
    position: absolute;
    left: 96px;
    top: 32px;
    width: 79px;
    height: 28px;
    background: var(--purple);
    color: var(--white);
    font: 500 20px/28px "Alegreya", serif;
    text-align: center;
  }
  .banner__last-name {
    position: absolute;
    left: 182px;
    top: 32px;
    color: var(--black);
    font: 500 20px/28px "Alegreya", serif;
  }
  .banner__stripe {
    position: absolute;
    left: 171px;
    top: 116px;
    width: 789px;
    height: 20px;
  }
  .banner__stripe--purple {
    background: linear-gradient(to bottom, var(--purple-light) 0%, var(--purple) 40%, var(--purple) 100%);
  }
  .banner__stripe--orange {
    background: linear-gradient(to bottom, var(--orange-light) 0%, var(--orange) 40%, var(--orange) 100%);
  }
  .banner__title {
    position: absolute;
    right: 10px;
    top: 66px;
    margin: 0;
    font: 400 42px/50px "Josefin Sans", sans-serif;
    font-variant: small-caps;
    letter-spacing: 6px;
    white-space: nowrap;
  }
  .banner__title--orange { color: var(--orange); }
  .banner__title--white  { color: var(--white); }
  .banner__title-accent  { color: var(--purple); }
  .banner__subtitle {
    position: absolute;
    right: 13px;
    top: 116px;
    margin: 0;
    font: 400 12.5px/20px "Alegreya", serif;
    white-space: nowrap;
  }
  .banner__subtitle--light { color: var(--white); }
  .banner__subtitle--dark  { color: var(--black); }
  .banner__subtitle--caps  { text-transform: uppercase; font-size: 12px; letter-spacing: 0.4px; }
</style>
</head>
<body>

  <section class="banner banner--one">
    <div class="banner__sky"></div>
    <div class="banner__skyline" role="img" aria-label="City skyline silhouette with world landmarks and a plane"></div>
    <div class="banner__name-band"></div>
    <div class="banner__portrait" role="img" aria-label="Portrait photo of the blogger"></div>
    <span class="banner__first-name">Colin</span>
    <span class="banner__last-name">Ashworth's</span>
    <div class="banner__stripe banner__stripe--purple"></div>
    <h1 class="banner__title banner__title--orange">Notes for Wanderers</h1>
    <p class="banner__subtitle banner__subtitle--light">luxurious destinations, transportation, accommodation and journeys</p>
  </section>

  <section class="banner banner--two">
    <div class="banner__sky"></div>
    <div class="banner__skyline" role="img" aria-label="City skyline silhouette with world landmarks and a plane"></div>
    <div class="banner__name-band"></div>
    <div class="banner__portrait" role="img" aria-label="Portrait photo of the blogger"></div>
    <span class="banner__first-name">Colin</span>
    <span class="banner__last-name">Ashworth's</span>
    <div class="banner__stripe banner__stripe--orange"></div>
    <h1 class="banner__title banner__title--orange">Notes for Wanderers</h1>
    <p class="banner__subtitle banner__subtitle--dark">luxurious destinations, transportation, accommodation and journeys</p>
  </section>

  <section class="banner banner--three">
    <div class="banner__sky"></div>
    <div class="banner__skyline" role="img" aria-label="City skyline silhouette with world landmarks and a plane"></div>
    <div class="banner__name-band"></div>
    <div class="banner__portrait" role="img" aria-label="Portrait photo of the blogger"></div>
    <span class="banner__first-name">Colin</span>
    <span class="banner__last-name">Ashworth's</span>
    <div class="banner__stripe banner__stripe--orange"></div>
    <h1 class="banner__title banner__title--white">Notes for <span class="banner__title-accent">Wanderers</span></h1>
    <p class="banner__subtitle banner__subtitle--dark banner__subtitle--caps">luxurious destinations, transportation, accommodation and journeys</p>
  </section>

  <section class="banner banner--four">
    <div class="banner__sky"></div>
    <div class="banner__skyline" role="img" aria-label="City skyline silhouette with world landmarks and a plane"></div>
    <div class="banner__name-band"></div>
    <div class="banner__portrait" role="img" aria-label="Portrait photo of the blogger"></div>
    <span class="banner__first-name">Colin</span>
    <span class="banner__last-name">Ashworth's</span>
    <div class="banner__stripe banner__stripe--purple"></div>
    <h1 class="banner__title banner__title--white">Notes for Wanderers</h1>
    <p class="banner__subtitle banner__subtitle--light">luxurious destinations, transportation, accommodation and journeys</p>
  </section>

</body>
</html>
```